Executive Taxi firm with Chauffeur service Website

I have my domain name registered and I have started to work on my site but I am struggling. I am just about to get a logo for the company and need a web site that clearly represents the fact we are an executive/luxury brand in private hire vehicles. We offer airport transfers, train station transfers, seaport transfers, holiday transfers and business to business pick up and drop off.

Target Market(s)

Corporate people, holidaymakers looking for a luxury start their holiday. VIPs' and celebrities.

Number of Pages Required

5+ page

Font styles to use
Serif
Sans Serif
Decorative
Script

Colors

Designer to choose colors to be used in the design.

Requirements
Must have
• Home Page, Services, About Us, VIP and Contact us
• Please see www.brookvane.co.uk I have started it but not happy with it at all.
Nice to have
• Booking form or enquiry form.

```html
<!DOCTYPE html>
<html lang="en">
<head>
<meta charset="utf-8">
<title>Private Hire, Chauffeur and Taxi Service</title>
<link href="https://fonts.googleapis.com/css2?family=Catamaran:wght@300;400;500;700;800&display=swap" rel="stylesheet">
<style>
:root{
  --yellow:#f5cf00;
  --ink:#1d1d1b;
  --dark:#22211c;
  --btn:#262624;
  --card:#e9e9e7;
  --white:#ffffff;
  --muted:#8a8a86;
  --field:#5c5c58;
}
*{margin:0;padding:0;box-sizing:border-box}
html,body{width:802px;height:1200px;overflow:hidden;background:var(--white)}
body{font-family:"Catamaran",sans-serif;color:var(--ink);position:relative}
.abs{position:absolute}

.hero{position:absolute;left:0;top:0;width:802px;height:338px;
  background:radial-gradient(ellipse at 70% 60%,#4a3516 0%,#2a1d0e 45%,#140e08 100%)}
.nav{position:absolute;top:26px;left:341px;display:flex;gap:0}
.nav a{position:absolute;color:#e8e8e8;text-decoration:none;font-size:10.5px;white-space:nowrap}
.hero-phone{position:absolute;left:607px;top:20px;display:flex;align-items:center;gap:8px;color:var(--yellow);font-size:16.5px;font-weight:300;letter-spacing:.2px}
.hero-title{position:absolute;left:40px;top:165px;width:302px;text-align:center;color:var(--white);font-size:17px;line-height:23px;font-weight:400}
.hero-title b{color:var(--yellow);font-weight:800}

.booking{position:absolute;left:370px;top:99px;width:232px;height:213px;background:var(--white)}
.booking-head{height:35px;background:var(--yellow);font-weight:700;font-size:11px;padding:12px 0 0 13px;letter-spacing:.2px}
.field{position:absolute;width:92px;border-bottom:1px solid #c9c9c9;font-size:7px;color:#6c6c6a;padding-bottom:3px}
.btn{position:absolute;background:var(--btn);color:var(--yellow);font-size:10px;display:flex;align-items:center;justify-content:center;border:1px solid #111}

.section-title{position:absolute;left:0;width:802px;text-align:center;font-size:17px}
.intro-art{position:absolute;left:0;top:440px;width:222px;height:80px;border-radius:30px 40px 8px 8px;background:linear-gradient(180deg,#f7d23a,#f0b400)}
.intro-text{position:absolute;left:267px;top:453px;width:470px;font-size:9.4px;line-height:23.5px;color:#222}

.card{position:absolute;top:743px;width:135px;height:124px;background:var(--card);text-align:center}
.card.active{background:var(--yellow)}
.card svg{position:absolute;left:50%;top:24px;transform:translateX(-50%)}
.card span{position:absolute;left:0;right:0;top:90px;font-size:11px;color:#222}

.callout{position:absolute;left:0;top:905px;width:802px;height:107px;background:var(--yellow);text-align:center}
.callout p{position:absolute;left:0;right:0;top:32px;font-size:13.5px;font-weight:500}
.callout .num{top:60px;font-size:19.5px;font-weight:300;letter-spacing:.4px}

.footer{position:absolute;left:0;top:1012px;width:802px;height:188px;background:var(--dark);color:var(--white)}
.footer h4{position:absolute;top:34px;font-size:13px;font-weight:500;letter-spacing:.5px}
.footer-links a{position:absolute;left:268px;color:#e4e4e4;text-decoration:none;font-size:10px}
.newsletter-text{position:absolute;left:374px;top:70px;font-size:9.5px;color:#dedede}
.newsletter-input{position:absolute;left:374px;top:92px;width:170px;height:24px;background:var(--field)}
.newsletter-btn{position:absolute;left:374px;top:124px;width:63px;height:20px;background:var(--yellow);color:var(--ink);font-size:10px;display:flex;align-items:center;justify-content:center}
.footer-map{position:absolute;left:589px;top:74px;width:146px;height:77px;background:linear-gradient(135deg,#4a4b4f,#3a3b3f)}
</style>
</head>
<body>

<header class="hero" role="img" aria-label="Night street scene with a taxi roof sign blurred in city lights">
  <nav class="nav">
    <a style="left:0;top:0">Home</a>
    <a style="left:49px;top:0">Services</a>
    <a style="left:109px;top:0">About</a>
    <a style="left:159px;top:0">Contact</a>
  </nav>
  <div class="hero-phone">
    <svg width="12" height="20" viewBox="0 0 12 20" fill="none" stroke="#f5cf00" stroke-width="1.2"><path d="M3 2 L6 5 L4.5 7.5 C5 10 6 12.5 8 14 L10 12.5 L11 16 L8.5 18 C4 16 1 10 1.5 4 Z"/></svg>
    07700 900461
  </div>
  <h1 class="hero-title"><b>PRIVATE HIRE,</b><br>CHAUFFEUR AND <b>TAXI SERVICE</b></h1>
</header>

<form class="booking">
  <div class="booking-head">BOOK A RIDE</div>
  <div class="field" style="left:13px;top:73px">First Name:</div>
  <div class="field" style="left:128px;top:73px">Last Name:</div>
  <div class="field" style="left:13px;top:103px">Email</div>
  <div class="field" style="left:128px;top:103px">Phone:</div>
  <div class="field" style="left:13px;top:130px">Date</div>
  <div class="field" style="left:128px;top:130px">Time</div>
  <div class="btn" style="left:52px;top:173px;width:113px;height:28px">Submit</div>
</form>

<h2 class="section-title" style="top:388px;font-weight:500">Always here for you</h2>
<div class="intro-art" role="img" aria-label="Illustration of a yellow taxi cab"></div>
<p class="intro-text">We provide airport transfers to and from all major UK airports, seaports, train station transfers and an executive business to business transfer service. Whether you have an individual or group transfer request, our company-owned fleet offers a choice of options to suit your needs, from luxury saloons and SUV's to 9-seat luxury transporters.</p>
<div class="btn" style="left:267px;top:574px;width:105px;height:32px;font-size:9px">Learn More</div>

<h2 class="section-title" style="top:677px;font-weight:300"><b style="font-weight:700">OUR</b> SERVICES</h2>

<div class="card" style="left:97px">
  <svg width="40" height="36" viewBox="0 0 40 36" fill="none" stroke="#1d1d1b" stroke-width="1.4" stroke-linejoin="round"><path d="M35 3 L30 4 L10 22 L5 21 L3 23 L9 26 L12 32 L14 30 L13 25 L32 7 Z M23 11 L12 8 L9 10 L19 15 M27 15 L30 26 L28 28 L23 19"/><path d="M2 34 L8 28 M5 35 L10 30"/></svg>
  <span>Airport Transfer</span>
</div>
<div class="card active" style="left:253px">
  <svg width="40" height="38" viewBox="0 0 40 38" fill="none" stroke="#ffffff" stroke-width="1.4" stroke-linejoin="round"><path d="M17 4 H23 V10 H17 Z M11 10 H29 V18 H11 Z M5 18 H35 L31 30 H9 Z"/><path d="M15 14 H17 M23 14 H25"/><path d="M3 34 C7 31 10 37 14 34 C18 31 22 37 26 34 C30 31 33 37 37 34"/></svg>
  <span>Seaport&nbsp; Transfer</span>
</div>
<div class="card" style="left:410px">
  <svg width="34" height="38" viewBox="0 0 34 38" fill="none" stroke="#1d1d1b" stroke-width="1.6" stroke-linejoin="round"><rect x="4" y="2" width="26" height="28" rx="4"/><path d="M8 7 H26 V18 H8 Z M17 7 V18"/><circle cx="10" cy="24" r="1.6"/><circle cx="24" cy="24" r="1.6"/><path d="M8 30 L3 36 M26 30 L31 36 M6 34 H28"/></svg>
  <span>Train Station&nbsp; Transfer</span>
</div>
<div class="card" style="left:567px">
  <svg width="40" height="40" viewBox="0 0 40 40" fill="none" stroke="#1d1d1b" stroke-width="1.5" stroke-linejoin="round"><path d="M20 30 C14 22 11 17 11 12 A9 9 0 0 1 29 12 C29 17 26 22 20 30 Z"/><circle cx="20" cy="12" r="4"/><path d="M14 26 H8 L3 37 H37 L32 26 H26 M11 31 L29 31"/></svg>
  <span>Pick up and Drop off</span>
</div>

<section class="callout">
  <p>We are Ready to Take Your Call 24 Hours, 7 Days!</p>
  <p class="num">07700 900461</p>
</section>

<footer class="footer">
  <h4 style="left:268px">MENU</h4>
  <div class="footer-links">
    <a style="top:72px">Home</a>
    <a style="top:90px">Services</a>
    <a style="top:107px">About</a>
    <a style="top:125px">Contact</a>
  </div>
  <h4 style="left:374px">STAY CONNECTED</h4>
  <p class="newsletter-text">Join our newsletter and find out more.</p>
  <div class="newsletter-input"></div>
  <div class="newsletter-btn">Submit</div>
  <div class="footer-map" role="img" aria-label="Location map of the city centre with a marker"></div>
</footer>

</body>
</html>
```